High value cover design for an A4 ideation pad.

The product is NOT A BOOK.

It's an A4 ideation pad for professionals, designers and creators who handwrite their ideas. Visualise creators like Paul Menteith, Glen Usborne and Carl Whitmoor in your mind's eye.

I'm looking for a cover design for the ideation pad. Both front and back.

It should look, feel and convey the following.

--> A handcrafted product experience

--> High value & Elegance

--> Inspiration

Mandatory --> See Uploaded Files --> Files 1, 5 & 6

Target Market(s)

- Designers

-Creative Professionals

- Entrepreneurs

who handwrite their ideas. Visualise creators like Paul Menteith, Glen Usborne and Carl Whitmoor in your mind's eye.

Industry/Entity Type

Stationary

Font styles to use
Script
Other font styles liked:
• Calligraphy

Colors
fbed22

Requirements
Must have
• Title text - Ink And Iron

-Text in gold on brown leather background to convey high value for the front cover.

--> High value & Elegance

--> Inspiration

--> Should compel the customers to pick up and own the idea pad
Nice to have
• That's my take but other ideas are welcome
Should not have
• Must not convey

- low value

```html
<!DOCTYPE html>
<html lang="en">
<head>
<meta charset="utf-8">
<title>Ink And Iron — Ideation Pad Covers</title>
<link rel="stylesheet" href="https://fonts.googleapis.com/css2?family=Allura&display=swap">
<style>
  :root {
    --backdrop: #f3f3f3;
    --leather: #a44e1e;
    --leather-light: #b05a27;
    --leather-dark: #93431a;
    --grain: #4a1e08;
    --gold-light: #fbed22;
    --gold-bright: #e9c232;
    --gold-mid: #d4a226;
    --gold-deep: #b07f18;
  }
  * { margin: 0; padding: 0; box-sizing: border-box; }
  html, body {
    width: 1200px;
    height: 828px;
    overflow: hidden;
    background: var(--backdrop);
  }
  .canvas {
    position: relative;
    width: 1200px;
    height: 828px;
  }
  .cover {
    position: absolute;
    top: 135px;
    width: 367px;
    height: 498px;
    overflow: hidden;
    background:
      radial-gradient(ellipse at 30% 20%, var(--leather-light) 0%, transparent 60%),
      radial-gradient(ellipse at 75% 90%, var(--leather-dark) 0%, transparent 65%),
      var(--leather);
  }
  .cover--front { left: 151px; }
  .cover--back { left: 674px; }
  .cover__grain {
    position: absolute;
    inset: 0;
    width: 100%;
    height: 100%;
    opacity: 0.35;
    mix-blend-mode: multiply;
  }
  .title {
    position: absolute;
    inset: 0;
  }
  .title__line {
    position: absolute;
    left: 0;
    width: 100%;
    text-align: center;
    font-family: "Allura", cursive;
    font-weight: 400;
    line-height: 1;
    white-space: nowrap;
    background: linear-gradient(100deg, var(--gold-deep) 0%, var(--gold-bright) 30%, var(--gold-light) 45%, var(--gold-mid) 70%, var(--gold-deep) 100%);
    -webkit-background-clip: text;
    background-clip: text;
    color: transparent;
  }
  .title__lead {
    top: 62px;
    font-size: 62px;
    padding-left: 8px;
  }
  .title__main {
    top: 168px;
    font-size: 168px;
    padding-right: 4px;
  }
</style>
</head>
<body>
  <svg width="0" height="0" style="position:absolute" aria-hidden="true">
    <filter id="leather-grain" x="0" y="0" width="100%" height="100%">
      <feTurbulence type="fractalNoise" baseFrequency="0.85" numOctaves="3" seed="7" result="noise"/>
      <feColorMatrix type="matrix" values="0 0 0 0 0.29  0 0 0 0 0.12  0 0 0 0 0.03  0 0 0 1.6 -0.55"/>
    </filter>
  </svg>
  <main class="canvas">
    <section class="cover cover--front" aria-label="Front cover">
      <svg class="cover__grain" aria-hidden="true"><rect width="100%" height="100%" filter="url(#leather-grain)"/></svg>
      <h1 class="title">
        <span class="title__line title__lead">Ink And</span>
        <span class="title__line title__main">Iron</span>
      </h1>
    </section>
    <section class="cover cover--back" aria-label="Back cover">
      <svg class="cover__grain" aria-hidden="true"><rect width="100%" height="100%" filter="url(#leather-grain)"/></svg>
    </section>
  </main>
</body>
</html>
```